Invitation card to the opening of BRISKORA FITNESS CLUB

A successful training plan starts with BRISKORA Fitness!
Join us for our grand opening! OPEN HOUSE AND YOU ARE INVITED!
Tuesday 1st of August, 2017
Classes start from 7.30am till 9.30pm.
Explore the most fun, exciting, challenging and effective training system in the region.
Healthy drinks and delicious food will be provided.
We hope to see you there!

www.briskorafitnessclub.example
APP: BRISKORAFITNAB
Tel: 71-42 58 19

Industry/Entity Type

Fitness

Colors

Designer to choose colors to be used in the design.

Requirements
Must have
• Elegant card
Nice to have
• Logo in the background
Should not have
• pictures

```html
<!DOCTYPE html>
<html lang="en">
<head>
<meta charset="utf-8">
<title>BRISKORA Fitness – Grand Opening Invitation</title>
<link rel="stylesheet" href="https://fonts.googleapis.com/css2?family=Marcellus&family=Montserrat:wght@300;400;600;700&family=Great+Vibes&display=swap">
<style>
  :root {
    --backdrop: #b3bac0;
    --paper: #fbfbfa;
    --ink: #1c1c1c;
    --ink-soft: #4a4a4a;
    --gold: #9c8148;
    --gold-light: #d9c697;
    --silver: #d4d5d7;
    --silver-dark: #a9aaad;
  }
  * { margin: 0; padding: 0; box-sizing: border-box; }
  html, body { width: 1200px; height: 960px; overflow: hidden; }
  body { background: var(--backdrop); position: relative; font-family: "Montserrat", sans-serif; }

  .invitation-card {
    position: absolute; left: 100px; top: 135px;
    width: 1000px; height: 690px;
    background: var(--paper);
    box-shadow: 0 18px 40px rgba(0,0,0,0.22);
    overflow: hidden;
  }
  .card-art { position: absolute; inset: 0; }

  .invite-text {
    position: absolute; left: 30px; top: 44px; width: 680px;
    text-align: center; color: var(--ink-soft);
  }
  .tagline { font-weight: 400; font-size: 19px; letter-spacing: 3px; color: var(--ink); }
  .tagline strong { font-weight: 700; }
  .brand-name {
    font-family: "Marcellus", serif; font-size: 92px; line-height: 1;
    letter-spacing: 4px; color: var(--ink); margin-top: 12px;
  }
  .brand-sub {
    font-weight: 300; font-size: 26px; letter-spacing: 16px; color: var(--ink);
    margin-top: 2px; padding-left: 16px;
  }
  .lead-in { font-family: "Great Vibes", cursive; font-size: 32px; color: var(--gold); margin-top: 14px; }
  .headline { font-family: "Great Vibes", cursive; font-size: 66px; line-height: 1; color: var(--gold); }
  .body-copy { font-size: 19px; font-weight: 300; line-height: 1.4; margin-top: 14px; }
  .body-copy strong { font-weight: 600; color: var(--ink); }
  .body-copy + .body-copy { margin-top: 10px; }
  .sign-off { font-family: "Great Vibes", cursive; font-size: 42px; color: var(--gold); margin-top: 14px; }

  .contact-block {
    position: absolute; left: 786px; top: 120px; width: 206px;
    text-align: center; color: var(--ink);
  }
  .contact-mark {
    width: 34px; height: 34px; border-radius: 50%;
    border: 2px solid var(--gold); margin: 0 auto 10px;
  }
  .contact-name { font-family: "Marcellus", serif; font-size: 34px; line-height: 1; }
  .contact-sub { font-size: 11px; letter-spacing: 6px; font-weight: 300; margin-top: 2px; padding-left: 6px; }
  .contact-lines { margin-top: 20px; font-size: 12px; line-height: 1.6; color: var(--ink-soft); white-space: nowrap; }
  .contact-lines .web { font-weight: 700; font-size: 10.5px; color: var(--ink); }
</style>
</head>
<body>
  <article class="invitation-card">
    <svg class="card-art" viewBox="0 0 1000 690" width="1000" height="690">
      <defs>
        <linearGradient id="sparkleTone" x1="0" y1="0" x2="0.3" y2="1">
          <stop offset="0" stop-color="#e6e6e7"/>
          <stop offset="0.55" stop-color="#c3c4c6"/>
          <stop offset="1" stop-color="#b9b2a0"/>
        </linearGradient>
        <linearGradient id="goldTone" x1="0" y1="0" x2="0" y2="1">
          <stop offset="0" stop-color="#d9c697" stop-opacity="0"/>
          <stop offset="0.5" stop-color="#c9b177"/>
          <stop offset="1" stop-color="#a88f58"/>
        </linearGradient>
      </defs>
      <circle cx="320" cy="420" r="190" fill="none" stroke="#ececec" stroke-width="26"/>
      <path d="M750 0 C 810 250, 770 520, 620 690 L 1000 690 L 1000 0 Z"
            fill="url(#sparkleTone)" role="img" aria-label="Soft silver and gold sparkle backdrop"/>
      <path d="M780 300 C 770 480, 710 600, 620 690 L 820 690 C 850 560, 820 420, 780 300 Z"
            fill="url(#goldTone)" opacity="0.85"/>
      <path d="M750 0 C 810 250, 770 520, 620 690" fill="none" stroke="#c8b27c" stroke-width="4"/>
      <path d="M732 0 C 790 250, 752 520, 602 690" fill="none" stroke="#e4e4e4" stroke-width="3"/>
    </svg>

    <section class="invite-text">
      <p class="tagline">A <strong>SUCCESSFUL TRAINING PLAN STARTS WITH</strong></p>
      <h1 class="brand-name">BRISKORA</h1>
      <p class="brand-sub">FITNESS</p>
      <p class="lead-in">Join us for our</p>
      <h2 class="headline">Grand Opening!</h2>
      <p class="body-copy">OPEN HOUSE AND YOU ARE INVITED!</p>
      <p class="body-copy">Tuesday 1st of <strong>August, 2017</strong><br>Classes start from <strong>7.30am till 9.30pm.</strong></p>
      <p class="body-copy">Explore the most fun, exciting, challenging and effective<br>training system in the region.</p>
      <p class="body-copy">Healthy drinks and delicious food will be provided.</p>
      <p class="sign-off">We hope to see you there!</p>
    </section>

    <aside class="contact-block">
      <div class="contact-mark"></div>
      <p class="contact-name">BRISKORA</p>
      <p class="contact-sub">FITNESS</p>
      <p class="contact-lines">
        <span class="web">www.briskorafitnessclub.example</span><br>
        APP: BRISKORAFITNAB<br>
        TEL: 71-42 58 19
      </p>
    </aside>
  </article>
</body>
</html>
```